Investment Management Marketing Presentation

We need a PowerPoint presentation to introduce our new company to prospective investment clients. We are a small, new firm but our founders have 25+ years experience. We pursue an active, very different investment approach that has been very successful. Please see the attached Word doc for additional guidance.

Target Market(s)

Financial institutions, wealthy individuals

Industry/Entity Type

Investment Advisory

Font styles to use
Sans Serif

Colors
3176b5

Requirements
Should not have
• Too many stock photos. Graphic elements are better.

```html
<!DOCTYPE html>
<html lang="en">
<head>
<meta charset="utf-8">
<title>Harbor Peak Capital – US Small Cap Growth Strategy</title>
<link rel="stylesheet" href="https://fonts.googleapis.com/css2?family=Oswald:wght@500&family=Lora:wght@400;500&family=Open+Sans:wght@400;700&display=swap">
<style>
:root{
  --brand:#3176b5;
  --brand-light:#6ea6dc;
  --navy:#1e2a55;
  --ink:#2b2b33;
  --muted:#666a73;
  --paper:#ffffff;
  --stage-top:#f1f1f1;
  --stage:#8e8e8e;
  --night-1:#1b2740;
  --night-2:#34476a;
}
*{box-sizing:border-box;margin:0;padding:0}
html,body{width:732px;height:1200px;overflow:hidden}
body{position:relative;background:var(--stage);font-family:"Open Sans",Arial,sans-serif;color:var(--ink)}
.stage-top{position:absolute;left:0;top:0;width:732px;height:444px;background:var(--stage-top)}
.slide{position:absolute;width:342px;height:192px;background:var(--paper);overflow:hidden;box-shadow:0 8px 14px rgba(0,0,0,.28)}
.hero{left:24px;top:28px;transform:scale(2);transform-origin:0 0;box-shadow:0 4px 7px rgba(0,0,0,.2)}
.fill{position:absolute}
.footer{position:absolute;left:10px;bottom:8px;font-size:3.6px;color:var(--muted)}
.page-no{position:absolute;right:8px;bottom:6px;width:10px;height:10px;background:var(--brand);color:#fff;font-size:3.8px;display:flex;align-items:center;justify-content:center;border-radius:1.5px}
.serif-head{position:absolute;font-family:"Lora",Georgia,serif;font-weight:400;font-size:11.5px;color:var(--ink)}
.label{font-size:4.2px;font-weight:700;color:var(--brand);letter-spacing:.1px;margin:0 0 3px}
.bullets{list-style:none}
.bullets li{position:relative;font-size:3.6px;line-height:4.6px;color:var(--ink);padding-left:7px;margin-bottom:4.2px}
.bullets li::before{content:"";position:absolute;left:1px;top:1.4px;width:2.2px;height:2.2px;border-radius:50%;background:var(--navy)}
/* title slide */
.title-scene{inset:0;background:linear-gradient(180deg,#2a3557 0%,#3e4f74 40%,#23324f 62%,#1c2a44 100%)}
.title-band{position:absolute;left:160px;top:66px;width:182px;height:45px;background:rgba(49,118,181,.85);padding:6px 8px 0 28px;text-align:right;color:#fff}
.title-band h1{font-family:"Oswald",Arial,sans-serif;font-weight:500;font-size:14px;line-height:16px;letter-spacing:-.1px;text-align:left}
.title-band p{font-size:4.2px;font-weight:700;margin-top:3px}
.brand-seal{position:absolute;left:59px;top:71px;width:88px;height:88px;border-radius:50%;background:#fff;border:3.5px solid var(--navy);display:flex;align-items:center;justify-content:center;text-align:center}
.brand-seal span{font-family:"Lora",Georgia,serif;font-size:9px;line-height:10.5px;color:var(--navy)}
/* contents */
.toc-title{left:208px;top:20px;color:var(--brand)}
.toc{position:absolute;left:209px;top:41px;width:115px;list-style:none}
.toc li{display:flex;justify-content:space-between;font-size:3.6px;line-height:6px;color:var(--ink)}
/* overview */
.ov-head{left:25px;top:26px}
.ov-body{position:absolute;left:25px;top:60px;width:150px}
.ov-body .label{margin-top:0}
.ov-body .gap{height:6px}
/* vision */
.vision-panel{left:0;top:0;width:80px;height:192px;background:linear-gradient(170deg,#2f6fae 0%,#3a82c6 45%,#2c66a3 100%)}
.vision-frame{position:absolute;left:6px;top:7px;width:70px;height:178px;border:.8px solid rgba(255,255,255,.55)}
.vision-head{left:104px;top:32px}
.vision-body{position:absolute;left:104px;top:58px;width:228px}
.vision-body .label{margin-bottom:2px}
.vision-body .bullets{margin-bottom:6px}
.two-col{display:flex;gap:12px}
.two-col .bullets{flex:1}
.team-frame{position:absolute;left:238px;top:22px;width:80px;height:77px;border:.9px solid var(--brand)}
.team-photo{left:230px;top:0;width:78px;height:90px;background:linear-gradient(160deg,#d9dde3,#9aa3ad 60%,#5d6a7a)}
/* boldly */
.bold-block{left:0;top:0;width:88px;height:76px;background:linear-gradient(150deg,#5b93cb,#3176b5)}
.bold-frame{position:absolute;left:4px;top:4px;width:38px;height:66px;border:.8px solid rgba(255,255,255,.6)}
.bold-head{left:49px;top:66px}
.bold-cols{position:absolute;left:22px;top:100px;display:flex;gap:20px}
.bold-cols .label{font-size:3.8px}
.bold-photo{left:250px;top:0;width:92px;height:192px;background:linear-gradient(160deg,#0f1115,#2a2d33 50%,#4b4f57 100%)}
/* brand panel */
.brand-panel{position:absolute;left:374px;top:900px;width:342px;height:192px;display:flex;align-items:center;justify-content:center}
.brand-panel span{font-family:"Lora",Georgia,serif;font-size:26px;color:#fff;letter-spacing:1px}
</style>
</head>
<body>
<div class="stage-top"></div>

<!-- hero title slide -->
<section class="slide hero">
  <div class="fill title-scene" role="img" aria-label="Dusk photograph of a wooden pier leading to a castle across a still lake"></div>
  <div class="brand-seal"><span>Harbor Peak<br>Capital</span></div>
  <div class="title-band">
    <h1>US SMALL CAP GROWTH STRATEGY</h1>
    <p>DANIEL REYES, CHIEF INVESTMENT OFFICER</p>
    <p>APRIL 2019</p>
  </div>
</section>

<!-- title slide -->
<section class="slide" style="left:16px;top:468px">
  <div class="fill title-scene" role="img" aria-label="Dusk photograph of a wooden pier leading to a castle across a still lake"></div>
  <div class="brand-seal"><span>Harbor Peak<br>Capital</span></div>
  <div class="title-band">
    <h1>US SMALL CAP GROWTH STRATEGY</h1>
    <p>DANIEL REYES, CHIEF INVESTMENT OFFICER</p>
    <p>APRIL 2019</p>
  </div>
</section>

<!-- contents -->
<section class="slide" style="left:374px;top:468px">
  <svg class="fill" style="left:0;top:0" width="200" height="192" viewBox="0 0 200 192">
    <defs>
      <radialGradient id="umbrella" cx=".5" cy=".4" r=".6">
        <stop offset="0" stop-color="#7d858c"/><stop offset=".6" stop-color="#4c555d"/><stop offset="1" stop-color="#2c3238"/>
      </radialGradient>
    </defs>
    <circle cx="104" cy="92" r="76" fill="url(#umbrella)" role="img" aria-label="Photograph of a single red umbrella among many dark umbrellas"/>
    <circle cx="150" cy="150" r="42" fill="none" stroke="#fff" stroke-width="7"/>
    <circle cx="42" cy="34" r="12" fill="none" stroke="#9cc4ea" stroke-width="7"/>
  </svg>
  <h2 class="serif-head toc-title">Table of Contents</h2>
  <ul class="toc">
    <li><span>Overview</span><span>3</span></li>
    <li><span>Boldly Different</span><span>4</span></li>
    <li><span>Synergy Beyond the Style Box</span><span>5</span></li>
    <li><span>Leverages Two Alpha Drivers</span><span>6</span></li>
    <li><span>Philosophy and Process</span><span>7</span></li>
    <li><span>Bold Performance Objectives</span><span>8</span></li>
    <li><span>Investment Process</span><span>9</span></li>
    <li><span>Data and Screening</span><span>10</span></li>
    <li><span>Research and Analysis</span><span>11</span></li>
    <li><span>Stock Selection</span><span>12</span></li>
    <li><span>Portfolio Construction</span><span>13</span></li>
    <li><span>Monitor, Modify and Sell Discipline</span><span>14</span></li>
    <li><span>Risk Management</span><span>15</span></li>
    <li><span>Why Harbor Peak</span><span>16</span></li>
    <li><span>Exhibits</span><span>17</span></li>
    <li><span>Team</span><span>18</span></li>
    <li><span>Superior Performance Since 1999</span><span>19</span></li>
  </ul>
  <p class="footer">©2019 Harbor Peak Capital LLC</p>
  <span class="page-no">02</span>
</section>

<!-- overview -->
<section class="slide" style="left:16px;top:684px">
  <svg class="fill" style="left:0;top:0" width="342" height="192" viewBox="0 0 342 192">
    <polygon points="0,14 20,14 8,30" fill="var(--brand)"/>
    <polygon points="0,20 8,20 0,30" fill="#1f4f86"/>
    <polygon points="186,30 193,30 189.5,36" fill="var(--brand)"/>
    <defs>
      <linearGradient id="desk" x1="0" y1="0" x2="1" y2="1">
        <stop offset="0" stop-color="#8a6a4c"/><stop offset=".5" stop-color="#5e4632"/><stop offset="1" stop-color="#a9b4bf"/>
      </linearGradient>
    </defs>
    <polygon points="262,22 332,160 196,160" fill="url(#desk)" role="img" aria-label="Photograph of a business handshake over a desk with laptop and papers"/>
    <polygon points="262,14 340,164 180,164" fill="none" stroke="var(--brand)" stroke-width="1.2"/>
    <polygon points="200,74 214,100 186,100" fill="#c9cdd3"/>
    <polygon points="300,18 312,40 288,40" fill="#c9cdd3"/>
    <polygon points="214,88 232,118 196,118" fill="var(--brand)" opacity=".85"/>
    <polygon points="306,44 322,70 290,70" fill="var(--brand)" opacity=".85"/>
    <polygon points="190,112 200,128 180,128" fill="#1f4f86"/>
    <polygon points="324,60 332,74 316,74" fill="var(--brand)"/>
  </svg>
  <h2 class="serif-head ov-head">Harbor Peak Overview</h2>
  <div class="ov-body">
    <p class="label">WHO IS HARBOR PEAK</p>
    <ul class="bullets">
      <li>Denver based emerging US small-cap growth (SCG) active equity manager serving institutional investors.</li>
      <li>CIO Mark Ellison has over 25 years experience in fundamental growth investing.</li>
    </ul>
    <div class="gap"></div>
    <p class="label">WHY HARBOR PEAK</p>
    <ul class="bullets">
      <li>Investment industry evolution presents a business opportunity.</li>
      <li>Institutional demand for actively managed SCG equity.</li>
      <li>Proven history high-alpha low correlated returns.</li>
    </ul>
  </div>
  <p class="footer">©2019 Harbor Peak Capital LLC</p>
  <span class="page-no">03</span>
</section>

<!-- vision -->
<section class="slide" style="left:374px;top:684px">
  <div class="fill vision-panel" role="img" aria-label="Blue-tinted photograph of a mountain lake under a bright sky"></div>
  <div class="vision-frame"></div>
  <div class="team-frame"></div>
  <div class="fill team-photo" role="img" aria-label="Photograph of a team meeting in a bright office"></div>
  <h2 class="serif-head vision-head">Harbor Peak 2025</h2>
  <div class="vision-body">
    <p class="label">VISION</p>
    <ul class="bullets" style="width:110px"><li>To advise over $1 billion in assets and be recognized among the best US equity managers.</li></ul>
    <p class="label">MISSION</p>
    <ul class="bullets" style="width:110px"><li>To deliver high-alpha investment returns at low correlation over 3- and 5-year periods.</li></ul>
    <p class="label">MISSION</p>
    <div class="two-col">
      <ul class="bullets">
        <li>Consistent disciplined process</li>
        <li>Facts over forecasts</li>
        <li>Proprietary fundamental equity research</li>
      </ul>
      <ul class="bullets">
        <li>Concentrated, high conviction names with 90% active share</li>
        <li>Clarity and transparency in communications</li>
        <li>Outstanding client service</li>
      </ul>
    </div>
  </div>
  <span class="page-no">04</span>
</section>

<!-- boldly different -->
<section class="slide" style="left:16px;top:900px">
  <div class="fill bold-block" role="img" aria-label="Blue-tinted photograph of hands reviewing financial charts"></div>
  <div class="bold-frame"></div>
  <div class="fill bold-photo" role="img" aria-label="Photograph of a businessman in a dark suit reaching forward"></div>
  <h2 class="serif-head bold-head">Boldly Different</h2>
  <div class="bold-cols">
    <div>
      <p class="label">DEPARTING FROM BENCHMARKS</p>
      <ul class="bullets">
        <li>Concentrated and Selective</li>
        <li>High Conviction</li>
        <li>Moderate Turnover</li>
        <li>High Active Share</li>
      </ul>
    </div>
    <div>
      <p class="label">DELIVERS SUPERIOR PERFORMANCE</p>
      <ul class="bullets">
        <li>High Alpha</li>
        <li>Higher Sharpe Ratio</li>
        <li>Lower Beta</li>
        <li>Asymmetric Risk Profile</li>
        <li>Low Correlation</li>
      </ul>
    </div>
  </div>
  <p class="footer">©2019 Harbor Peak Capital LLC</p>
  <span class="page-no">05</span>
</section>

<!-- brand panel -->
<div class="brand-panel"><span>HARBOR PEAK CAPITAL</span></div>
</body>
</html>
```